Garden Design Flier

I would like a PDF of this half page A4 flier in soft green tones with dark green leaves.

Target Market(s)

Home owners and real estate agents

Font styles to use
Serif
Other font styles liked:
• Papyrus

Colors
acd136
9bcb3c
cadf82
fefdec

Requirements
Must have
• Green tones
Nice to have
• Leaves, vines, lawns
Should not have
• Open to ideas, but classic style

```html
<!DOCTYPE html>
<html lang="en">
<head>
<meta charset="utf-8">
<title>Verdance Gardens – Garden Design Flier</title>
<link rel="stylesheet" href="https://fonts.googleapis.com/css2?family=Macondo&display=swap">
<style>
  :root {
    --green-top: #a9cb5c;
    --green-mid: #cbe688;
    --green-bottom: #aace60;
    --ink: #1c2a0c;
    --frame: #22330f;
    --leaf-dark: rgba(44, 66, 22, 0.78);
    --leaf-line: rgba(104, 64, 20, 0.35);
  }
  html, body {
    margin: 0;
    padding: 0;
    width: 1200px;
    height: 852px;
    overflow: hidden;
    background: var(--green-mid);
  }
  .flyer {
    position: relative;
    width: 1200px;
    height: 852px;
    overflow: hidden;
    background: linear-gradient(to bottom, var(--green-top) 0%, var(--green-mid) 48%, var(--green-bottom) 100%);
    font-family: "Macondo", "Papyrus", fantasy;
    color: var(--ink);
  }
  .foliage {
    position: absolute;
    border-radius: 50%;
  }
  .foliage--top-left {
    left: -120px; top: -110px; width: 600px; height: 340px;
    background: radial-gradient(ellipse at 30% 40%, var(--leaf-dark) 0%, rgba(44,66,22,0.45) 45%, rgba(44,66,22,0) 72%);
  }
  .foliage--left {
    left: -90px; top: 190px; width: 270px; height: 170px;
    background: radial-gradient(ellipse at center, var(--leaf-line) 0%, rgba(104,64,20,0) 70%);
  }
  .foliage--top-right {
    left: 700px; top: -120px; width: 620px; height: 360px;
    background: radial-gradient(ellipse at 70% 40%, var(--leaf-dark) 0%, rgba(44,66,22,0.4) 45%, rgba(44,66,22,0) 72%);
  }
  .foliage--right {
    left: 1080px; top: 320px; width: 200px; height: 240px;
    background: radial-gradient(ellipse at 70% 50%, var(--leaf-line) 0%, rgba(104,64,20,0) 70%);
  }
  .foliage--bottom-left {
    left: -140px; top: 440px; width: 560px; height: 520px;
    background: radial-gradient(ellipse at 35% 65%, var(--leaf-dark) 0%, rgba(44,66,22,0.45) 45%, rgba(44,66,22,0) 72%);
  }
  .foliage--bottom-right {
    left: 580px; top: 620px; width: 720px; height: 340px;
    background: radial-gradient(ellipse at 70% 60%, var(--leaf-dark) 0%, rgba(44,66,22,0.4) 45%, rgba(44,66,22,0) 72%);
  }
  .frame {
    position: absolute;
    left: 0; top: 0;
    width: 1200px; height: 852px;
  }
  .brand-name {
    position: absolute;
    left: 0; width: 1200px;
    top: 118px;
    margin: 0;
    text-align: center;
    font-size: 94px;
    font-weight: 400;
    line-height: 1;
    letter-spacing: 1px;
  }
  .brand-sub {
    position: absolute;
    left: 0; width: 1200px;
    top: 228px;
    margin: 0;
    text-align: center;
    font-size: 30px;
    font-weight: 400;
    line-height: 1;
    letter-spacing: 30px;
    padding-left: 30px;
    box-sizing: border-box;
  }
  .owner {
    position: absolute;
    left: 0; width: 1200px;
    top: 296px;
    margin: 0;
    text-align: center;
    font-size: 32px;
    line-height: 1;
  }
  .credential {
    position: absolute;
    left: 0; width: 1200px;
    top: 350px;
    margin: 0;
    text-align: center;
    font-size: 23px;
    line-height: 1;
  }
  .services {
    position: absolute;
    top: 410px;
    left: 0; width: 1200px;
    margin: 0; padding: 0;
    list-style: none;
    font-size: 36px;
    line-height: 1;
  }
  .services li { position: absolute; top: 0; }
  .services li:nth-child(1) { left: 266px; }
  .services li:nth-child(2) { left: 440px; }
  .services li:nth-child(3) { left: 596px; }
  .services li:nth-child(4) { left: 736px; }
  .services li:nth-child(5) { left: 876px; }
  .pitch {
    position: absolute;
    left: 221px; top: 496px;
    width: 790px;
    margin: 0;
    font-size: 21px;
    line-height: 24px;
  }
  .contact {
    position: absolute;
    top: 603px;
    left: 0; width: 1200px;
    margin: 0;
    font-size: 20px;
    line-height: 1;
    font-style: normal;
  }
  .contact span { position: absolute; top: 0; white-space: nowrap; }
  .contact__email { left: 221px; }
  .contact__mobile { left: 639px; }
  .contact__abn { left: 900px; }
</style>
</head>
<body>
  <main class="flyer">
    <div class="foliage foliage--top-left" role="img" aria-label="Illustrated dark green leaves and vines in the top left corner"></div>
    <div class="foliage foliage--left" role="img" aria-label="Outlined leaf sketches along the left edge"></div>
    <div class="foliage foliage--top-right" role="img" aria-label="Illustrated dark green leaves and vines in the top right corner"></div>
    <div class="foliage foliage--right" role="img" aria-label="Outlined leaf sketches along the right edge"></div>
    <div class="foliage foliage--bottom-left" role="img" aria-label="Illustrated dark green leaves climbing from the bottom left corner"></div>
    <div class="foliage foliage--bottom-right" role="img" aria-label="Illustrated dark green leaves along the bottom right corner"></div>

    <svg class="frame" viewBox="0 0 1200 852" aria-hidden="true">
      <rect x="25" y="25" width="1149" height="798" fill="none" stroke="var(--frame)" stroke-width="3"/>
      <rect x="42" y="41" width="1114" height="765" fill="none" stroke="var(--frame)" stroke-width="2"/>
    </svg>

    <h1 class="brand-name">VERDANCE</h1>
    <p class="brand-sub">GARDENS</p>
    <p class="owner">by Callum Reeves</p>
    <p class="credential">Certificate 3. Horticulture. Greenvale College</p>

    <ul class="services">
      <li>Design</li>
      <li>Install</li>
      <li>Grow</li>
      <li>Tend</li>
      <li>Enjoy</li>
    </ul>

    <p class="pitch">All your gardening and landscaping needs from design and installation to general maintenance. Bespoke vegetable gardens and potager designs created to suit your site and requirements</p>

    <address class="contact">
      <span class="contact__email">Email: callum@verdancegardens.com.au</span>
      <span class="contact__mobile">Mobile: 0412-000318</span>
      <span class="contact__abn">ABN:41205573918</span>
    </address>
  </main>
</body>
</html>
```